Business Card Design for company

We want new business cards. We'd like something different-- yet still highly professional. Our tagline is Providing leadership, delivering success. Stock photos are ok, as long as they are relevant and look upscale.

Target Market(s)

Architecture/Business Management Consulting/Engineering Consulting

Contact Information for Business Card

dark gray background with pops of blue might be good, but you tell me. You're the designers. Rounded corners might be nice, but again, you tell me.

Font styles to use
Serif
Sans Serif

Colors
3276b5
5c5c5c
9d9d9d
fbfbfb

Requirements
Nice to have
• Something different, but still very professional.

```html
<!DOCTYPE html>
<html lang="en">
<head>
<meta charset="utf-8">
<title>Halvern International – Business Card</title>
<link rel="stylesheet" href="https://fonts.googleapis.com/css2?family=Montserrat:wght@400;500;600;700&display=swap">
<style>
  :root {
    --page: #ffffff;
    --paper: #f7f7f7;
    --slate: #37434c;
    --brand-blue: #0d4f8c;
    --accent-gray: #a9a9a9;
    --ink-light: #ffffff;
  }
  * { box-sizing: border-box; margin: 0; padding: 0; }
  html, body {
    width: 1200px; height: 1200px; overflow: hidden;
    background: var(--page);
    font-family: "Montserrat", sans-serif;
  }
  .canvas { position: relative; width: 1200px; height: 1200px; }
  .card {
    position: absolute; left: 243px; width: 714px; height: 410px;
    background: var(--paper); overflow: hidden;
  }
  .card--front { top: 93px; }
  .card--back { top: 696px; }
  .card__shapes { position: absolute; inset: 0; width: 714px; height: 410px; }
  .wordmark { position: absolute; color: var(--brand-blue); font-weight: 700; line-height: 1; }
  .wordmark__name { display: block; font-size: 46px; letter-spacing: 1px; }
  .wordmark__sub { display: block; font-size: 18px; letter-spacing: 1.5px; margin-top: 8px; }
  .card--front .wordmark { left: 77px; top: 52px; }
  .card--back .wordmark {
    left: 0; right: 0; top: 150px; text-align: center; color: var(--ink-light);
  }
  .card--back .wordmark__name { font-size: 78px; letter-spacing: 3px; }
  .card--back .wordmark__sub { font-size: 24px; letter-spacing: 2px; margin-top: 14px; }
  .person {
    position: absolute; right: 77px; top: 212px; text-align: right; color: var(--ink-light);
  }
  .person__name { font-size: 27px; font-weight: 500; letter-spacing: 1px; }
  .person__role { font-size: 19px; font-weight: 400; margin-top: 2px; }
  .contact-list {
    position: absolute; left: 77px; top: 262px; list-style: none; color: var(--ink-light);
    font-size: 15.5px; font-weight: 400;
  }
  .contact-list li { display: flex; align-items: center; height: 27px; }
  .contact-list svg { width: 14px; height: 14px; margin-right: 17px; fill: none; stroke: var(--ink-light); stroke-width: 1.4; }
  .website {
    position: absolute; right: 77px; top: 353px; color: var(--brand-blue);
    font-size: 16px; font-weight: 600; letter-spacing: 1px;
  }
</style>
</head>
<body>
<main class="canvas">

  <section class="card card--front">
    <svg class="card__shapes" viewBox="0 0 714 410" aria-hidden="true">
      <path fill="var(--brand-blue)" d="M210,208 Q480,172 714,64 L714,96 Q500,178 210,208 Z"/>
      <path fill="var(--slate)" d="M0,215 Q320,228 714,108 L714,312 Q560,300 100,410 L0,410 Z"/>
      <path fill="var(--accent-gray)" d="M60,410 Q260,358 470,330 Q300,352 130,410 Z"/>
    </svg>
    <div class="wordmark">
      <span class="wordmark__name">HALVERN</span>
      <span class="wordmark__sub">INTERNATIONAL</span>
    </div>
    <div class="person">
      <p class="person__name">ALEX MORGAN</p>
      <p class="person__role">Manager</p>
    </div>
    <ul class="contact-list">
      <li><svg viewBox="0 0 14 14"><rect x="3.5" y="1" width="7" height="12" rx="1"/><line x1="6" y1="11" x2="8" y2="11"/></svg>555-010-2481</li>
      <li><svg viewBox="0 0 14 14"><path d="M9 1.5 L7 3 Q4 6 5 10 L7 12.5 L9 11"/></svg>555-010-7734</li>
      <li><svg viewBox="0 0 14 14"><rect x="1.5" y="3.5" width="11" height="7"/><path d="M1.5 3.5 L7 8 L12.5 3.5"/></svg>alex.morgan@halvern.com</li>
    </ul>
    <p class="website">www.halvern.com</p>
  </section>

  <section class="card card--back">
    <svg class="card__shapes" viewBox="0 0 714 410" aria-hidden="true">
      <path fill="var(--brand-blue)" d="M210,86 Q440,62 525,0 L650,0 Q450,62 210,86 Z"/>
      <path fill="var(--slate)" d="M0,96 Q320,98 662,0 L714,0 L714,314 Q560,300 60,410 L0,410 Z"/>
      <path fill="var(--accent-gray)" d="M50,410 Q260,356 500,322 Q300,350 120,410 Z"/>
    </svg>
    <div class="wordmark">
      <span class="wordmark__name">HALVERN</span>
      <span class="wordmark__sub">INTERNATIONAL</span>
    </div>
  </section>

</main>
</body>
</html>
```